Authentic Log Lodge Requires Highway Signage (x2)

We are recently established Lodge and Cabins in Golden, BC, Canada. We already have a great reputation and have recently achieved a Wander Ledger Badge of Distinction - our guests love us and we love them.

Tamsworth Lodge is looking for two new signs;
1 - A highway sign (8ft high, 12ft wide) and a secondary directional sign (approx 3ft square). We have a strong brand and imagery and can supply photos and vectors. We are currently fighting an internal battle of how the highway sign should look - one option includes an image of the Lodge and the other is based around our logo. The design must include two items of text - "www.tamsworthlodge.example" and "Next Right"

2 - A directional sign. We would like this sign to be logo based and include a right facing arrow. The size of this sign can be flexible.

It would be great to establish a relationship with someone for future work.

We are in desperate need of some creative geniuses to don their superhero capes and come to our rescue.

Target Market(s)

Current guests looking to find us and prospective guests driving along the highway.

Industry/Entity Type

Hospitality

Font styles to use
Sans Serif

Colors

Designer to choose colors to be used in the design.

Requirements
Must have
• It must contain our logo and maintain the feel of our brand.
• It must be based on the brand colours (see attached documents).

```html
<!DOCTYPE html>
<html lang="en">
<head>
<meta charset="utf-8">
<title>Tamsworth Lodge – Highway Sign</title>
<link rel="stylesheet" href="https://fonts.googleapis.com/css2?family=Montserrat:wght@400;600&display=swap">
<style>
  :root {
    --paper: #ffffff;
    --sand: #ebe6d8;
    --olive: #8a8a3c;
    --ink: #2a2a2a;
    --gap: #ffffff;
    --sky-grey: #8f9296;
    --sky-blue: #6f9ccf;
    --log-wood: #9a5a2e;
    --log-dark: #6b3c1e;
    --forest: #3f5a3a;
    --gravel: #a9a49b;
    --lawn: #6f8f3e;
  }
  html, body {
    margin: 0;
    padding: 0;
    overflow: hidden;
    background: var(--paper);
  }
  .sign {
    position: relative;
    width: 1200px;
    height: 706px;
    overflow: hidden;
    background: var(--paper);
    font-family: "Montserrat", sans-serif;
  }
  .mosaic {
    position: absolute;
    inset: 0;
  }
  .mosaic polygon {
    stroke: var(--gap);
    stroke-width: 12;
    stroke-linejoin: miter;
  }
  .tile-sand { fill: var(--sand); }
  .brand-name {
    position: absolute;
    left: 944px;
    top: 262px;
    width: 226px;
    display: flex;
    align-items: center;
    justify-content: center;
    gap: 10px;
    color: var(--olive);
    font-weight: 600;
    font-size: 28px;
    letter-spacing: 2px;
    line-height: 1.1;
    text-align: center;
    text-transform: uppercase;
  }
  .brand-square {
    flex: none;
    width: 14px;
    height: 14px;
    background: var(--olive);
  }
  .direction {
    position: absolute;
    left: 836px;
    top: 514px;
    margin: 0;
    color: var(--ink);
    font-weight: 400;
    font-size: 34px;
    letter-spacing: 13px;
    white-space: nowrap;
  }
  .web-address {
    position: absolute;
    left: 836px;
    top: 556px;
    margin: 0;
    color: var(--ink);
    font-weight: 400;
    font-size: 15px;
    letter-spacing: 3.5px;
    white-space: nowrap;
  }
</style>
</head>
<body>
<main class="sign">
  <svg class="mosaic" width="1200" height="706" viewBox="0 0 1200 706">
    <defs>
      <linearGradient id="tone-sky" x1="0" y1="0" x2="0" y2="1">
        <stop offset="0" stop-color="var(--sky-grey)"/>
        <stop offset="1" stop-color="#5d6266"/>
      </linearGradient>
      <linearGradient id="tone-roof" x1="0" y1="0" x2="1" y2="1">
        <stop offset="0" stop-color="#8d9094"/>
        <stop offset="1" stop-color="#4c5653"/>
      </linearGradient>
      <linearGradient id="tone-wood" x1="0" y1="0" x2="0" y2="1">
        <stop offset="0" stop-color="var(--log-wood)"/>
        <stop offset="1" stop-color="var(--log-dark)"/>
      </linearGradient>
      <linearGradient id="tone-trees" x1="0" y1="0" x2="1" y2="1">
        <stop offset="0" stop-color="var(--forest)"/>
        <stop offset="1" stop-color="var(--sky-blue)"/>
      </linearGradient>
      <linearGradient id="tone-ground" x1="0" y1="0" x2="0" y2="1">
        <stop offset="0" stop-color="#8a6a4c"/>
        <stop offset="1" stop-color="var(--gravel)"/>
      </linearGradient>
      <linearGradient id="tone-lawn" x1="0" y1="0" x2="0" y2="1">
        <stop offset="0" stop-color="var(--gravel)"/>
        <stop offset="1" stop-color="var(--lawn)"/>
      </linearGradient>
    </defs>

    <!-- sand accent tiles -->
    <polygon class="tile-sand" points="-75,75 50,200 175,75 50,-50"/>
    <polygon class="tile-sand" points="-200,200 -75,325 50,200 -75,75"/>
    <polygon class="tile-sand" points="-75,575 55,705 180,580 50,450"/>
    <polygon class="tile-sand" points="550,-50 680,80 805,-45 675,-175"/>
    <polygon class="tile-sand" points="680,80 800,200 925,75 805,-45"/>
    <polygon class="tile-sand" points="805,-45 925,75 1050,-50 930,-170"/>
    <polygon class="tile-sand" points="675,575 800,700 925,575 800,450"/>
    <polygon class="tile-sand" points="800,700 925,825 1050,700 925,575"/>

    <!-- lodge photo mosaic -->
    <polygon fill="url(#tone-sky)" points="50,200 175,325 300,200 175,75" role="img" aria-label="Photo: cloudy sky over the lodge roof"/>
    <polygon fill="url(#tone-roof)" points="175,75 300,200 425,75 300,-50" role="img" aria-label="Photo: dark green shingle roof under grey clouds"/>
    <polygon fill="url(#tone-wood)" points="300,200 430,330 555,205 425,75" role="img" aria-label="Photo: log gable with balcony and green window trim"/>
    <polygon fill="url(#tone-wood)" points="175,325 305,455 430,330 300,200" role="img" aria-label="Photo: log walls and red deck railing"/>
    <polygon fill="url(#tone-wood)" points="-75,325 50,450 175,325 50,200" role="img" aria-label="Photo: stacked log corner of the lodge"/>
    <polygon fill="url(#tone-ground)" points="50,450 180,580 305,455 175,325" role="img" aria-label="Photo: deck railing over stone foundation"/>
    <polygon fill="url(#tone-ground)" points="180,580 300,700 425,575 305,455" role="img" aria-label="Photo: boulders beside the gravel driveway"/>
    <polygon fill="url(#tone-ground)" points="305,455 425,575 550,450 430,330" role="img" aria-label="Photo: entrance steps and rock garden"/>
    <polygon fill="url(#tone-wood)" points="430,330 550,450 675,325 555,205" role="img" aria-label="Photo: wraparound deck with red railing"/>
    <polygon fill="url(#tone-trees)" points="425,75 555,205 680,80 550,-50" role="img" aria-label="Photo: tall evergreens against blue sky"/>
    <polygon fill="url(#tone-trees)" points="555,205 675,325 800,200 680,80" role="img" aria-label="Photo: stone chimney among trees"/>
    <polygon fill="url(#tone-lawn)" points="550,450 675,575 800,450 675,325" role="img" aria-label="Photo: driveway edge and shrubs"/>
    <polygon fill="url(#tone-lawn)" points="425,575 550,700 675,575 550,450" role="img" aria-label="Photo: gravel drive and green lawn"/>
    <polygon fill="url(#tone-trees)" points="675,325 800,450 925,325 800,200" role="img" aria-label="Photo: side deck with patio umbrella and forest"/>
    <polygon fill="url(#tone-lawn)" points="300,700 425,825 550,700 425,575" role="img" aria-label="Photo: lawn in the foreground"/>
  </svg>

  <div class="brand-name">
    <span class="brand-square"></span>
    <span>Tamsworth<br>Lodge</span>
  </div>

  <p class="direction">NEXT RIGHT</p>
  <p class="web-address">www.tamsworthlodge.example</p>
</main>
</body>
</html>
```